Honey jar label for small US farm

My daughters have 6 beehives and will be producing 300-400 jars of honey this season that they plan to sell at the farmers' market.
We are looking for a label design for small honey jars.
Label size:  1.5 inches high and 3 inches wide.
The label will be a simple RECTANGLE (no special cut)
We would like a playful look but upscale enough. We don't think that flowers or bees add anything. We like cleaner looks but not cold.
Maybe one could also represent the 3 sisters somewhere on the label. As elegant stick figures maybe?
One could also imagine a design where the label is black and the text/images are white to add some dramatic effect. The jar lid is black.
The honey is raw, un-pasturized, straight from the beehive.

Target Market(s)
Farm stand, sold by the 3 sisters who are 11, 9 and 6
Industry/Entity Type
Food Production
Colors
Designer to choose colors to be used in the design.
Requirements
Must have
- Name (means three sisters in English): Clos Ardent
- What it is: Ashbrooke Raw Honey
- Net weight: 3.75oz (110ml)
- Location: Fernwick, VT
- Text on one of the sides: Sister to sister we will always be, a couple of nuts off the family tree!
- Note that the jar is an hexagon. See the attached STOCK photo.
- Therefore, a little more than 1 inch is on the front facing, and 0.75 inches on each sides.

Nice to have
- The design should be elegant (but not ornate), but clean. Inviting and fun.
- No need for bees or flowers which would not make it look upscale.
- No gold or "over the top" fancy. Modern but not cold.
- Remember that this is a honey brand for 3 young sisters. Something playful but upscale would work too.
- Not sure about color codes. We are quite happy staying in grey scales, but a little bit of colour might work too.

Should not have
- No UPC code needed

```html
<!DOCTYPE html>
<html lang="en">
<head>
<meta charset="utf-8">
<title>Clos Ardent – Ashbrooke Raw Honey Label</title>
<link rel="stylesheet" href="https://fonts.googleapis.com/css2?family=Kanit:wght@600&family=Lato:wght@400&display=swap">
<style>
  :root {
    --backdrop: #c9cacc;
    --label-light: #e6e7e8;
    --comb-fill: #dcdddf;
    --band-dark: #3a3a3c;
    --hex-line: #ffffff;
    --text-light: #ffffff;
    --text-dark: #3a3a3c;
  }
  * { margin: 0; padding: 0; box-sizing: border-box; }
  html, body {
    width: 1200px;
    height: 678px;
    overflow: hidden;
    background: var(--backdrop);
  }
  .canvas {
    position: relative;
    width: 1200px;
    height: 678px;
  }
  .label {
    position: absolute;
    left: 40px;
    top: 59px;
    width: 1303px;
    height: 651px;
    transform: scale(0.8596);
    transform-origin: 0 0;
    background: var(--label-light);
    overflow: hidden;
  }
  .label-shapes {
    position: absolute;
    inset: 0;
    width: 1303px;
    height: 651px;
  }
  .comb-panel { fill: var(--comb-fill); }
  .side-band { fill: var(--band-dark); }
  .center-hex { fill: var(--label-light); stroke: var(--hex-line); stroke-width: 5; }
  .cap-hex { fill: var(--band-dark); }

  .brand-name,
  .product-name,
  .net-weight,
  .location,
  .family-motto {
    position: absolute;
    white-space: nowrap;
  }
  .brand-name {
    left: 401px;
    width: 500px;
    top: 70px;
    text-align: center;
    font-family: "Kanit", sans-serif;
    font-weight: 600;
    font-size: 56px;
    line-height: 1;
    color: var(--text-light);
  }
  .product-name {
    left: 263px;
    width: 778px;
    top: 270px;
    text-align: center;
    font-family: "Kanit", sans-serif;
    font-weight: 600;
    font-size: 92px;
    line-height: 87px;
    letter-spacing: -1px;
    color: var(--text-dark);
  }
  .net-weight {
    left: 433px;
    width: 436px;
    top: 581px;
    text-align: center;
    font-family: "Lato", sans-serif;
    font-size: 32px;
    line-height: 1;
    color: var(--text-light);
  }
  .location {
    left: 37px;
    top: 307px;
    font-family: "Lato", sans-serif;
    font-size: 27px;
    line-height: 1;
    color: var(--text-light);
  }
  .family-motto {
    right: 39px;
    top: 255px;
    text-align: right;
    font-family: "Lato", sans-serif;
    font-size: 27px;
    line-height: 36px;
    color: var(--text-light);
  }
</style>
</head>
<body>
<div class="canvas">
  <div class="label">
    <svg class="label-shapes" viewBox="0 0 1303 651" xmlns="http://www.w3.org/2000/svg">
      <g role="img" aria-label="Light grey honeycomb pattern background">
        <rect class="comb-panel" x="0" y="0" width="1303" height="223"/>
        <rect class="comb-panel" x="0" y="465" width="1303" height="186"/>
      </g>
      <rect class="side-band" x="0" y="223" width="1303" height="242"/>
      <polygon class="center-hex" points="458,-3 844,-3 1041,324 844,654 458,654 263,324"/>
      <polygon class="cap-hex" points="459,0 843,0 901,101 844,203 457,203 401,101"/>
      <polygon class="cap-hex" points="476,555 844,555 869,603 844,651 458,651 433,603"/>
    </svg>

    <div class="brand-name">CLOS ARDENT</div>
    <h1 class="product-name">ASHBROOKE<br>RAW HONEY</h1>
    <div class="net-weight">3.75oz (110ml)</div>
    <div class="location">Fernwick, VT</div>
    <p class="family-motto">Sister to sister<br>we will always<br>be, a couple<br>of nuts off the<br>family tree!</p>
  </div>
</div>
</body>
</html>
```